Incense Box and Outer Box Design

Require new package design with Die Lines for 6 fragrances: Dragon's Blood, Frankincense & Myrrh, Patchouli, Gentle Meadow, Dusk Tide, and White Sage.
25cm long incense sticks and 30x per box or tube.
We need really creative box design and solutions here. Not after standard box designs that all other incense sellers are doing.
Really need to think outside the "box" on this one.
Brand name is Kelvoro but this logo does NOT have to be prominent. There needs to be space for a GS1 barcode (which will be provided).

Target Market(s)

Yoga, Health, Religious

Font styles to use
Decorative

Requirements
Must have
• Classy and premium design. No tacky or cheap stock images or logo.\
Nice to have
• Bold, standout and bright.

Would love the cap or the box be an incense holder as well.
Should not have
• Cheap stock images

```html
<!DOCTYPE html>
<html lang="en">
<head>
<meta charset="utf-8">
<title>Kelvoro White Sage Incense Box</title>
<link href="https://fonts.googleapis.com/css2?family=Oswald:wght@300;400&family=Roboto+Slab:wght@300;400;700&family=Rye&display=swap" rel="stylesheet">
<style>
  :root {
    --stage: #e4ebea;
    --paper: #ededee;
    --paper-shade: #e1e2e4;
    --teal: #137a77;
    --teal-deep: #0d5f5e;
    --teal-bright: #1fb5b8;
    --gold: #c99a2e;
    --gold-light: #e6bb52;
    --ink: #3b3b3b;
    --black: #161616;
    --white: #ffffff;
  }
  * { box-sizing: border-box; margin: 0; padding: 0; }
  html, body { width: 900px; height: 1200px; overflow: hidden; }
  body { background: var(--stage); position: relative; font-family: "Roboto Slab", serif; }

  .box { position: absolute; top: 100px; left: 130px; width: 640px; height: 1000px; display: flex; }

  .panel { position: relative; height: 100%; background: var(--paper); }
  .panel-side { width: 200px; background: var(--paper-shade); border-right: 1px solid #cfd0d2; }
  .panel-front { width: 440px; }

  .band-rule { position: absolute; left: 0; right: 0; top: 742px; height: 14px;
    background: linear-gradient(var(--black) 0 5px, #dcdcdc 5px 8px, var(--black) 8px 14px); }
  .band { position: absolute; left: 0; right: 0; top: 756px; bottom: 0; background: var(--teal); color: var(--white); text-align: center; }

  /* Side panel */
  .side-mark { position: absolute; top: 78px; left: 50%; transform: translateX(-50%); width: 58px; height: 88px;
    background: linear-gradient(135deg, var(--gold-light), var(--gold)); }
  .side-title { position: absolute; top: 214px; left: 0; right: 0; text-align: center; font-family: "Oswald", sans-serif; }
  .side-title .kind { display: block; color: var(--teal); font-size: 17px; font-weight: 400; letter-spacing: 0.2px; }
  .side-title .item { display: block; color: var(--ink); font-size: 17px; font-weight: 300; margin-top: 2px; }
  .side-copy { position: absolute; top: 300px; left: 18px; right: 18px; font-family: "Oswald", sans-serif; font-weight: 300;
    font-size: 10.5px; line-height: 14px; color: #2a2a2a; text-align: justify; hyphens: auto; }
  .side-web { display: block; margin-top: 84px; font-family: "Roboto Slab", serif; font-weight: 700; font-size: 15px; }

  /* Front panel */
  .brand { position: absolute; top: 110px; left: 0; right: 0; display: flex; justify-content: center; align-items: center; gap: 10px; }
  .brand-square { width: 44px; height: 44px; background: var(--gold); }
  .brand-name { font-family: "Roboto Slab", serif; font-weight: 400; font-size: 40px; color: var(--gold); line-height: 1; }

  .cartouche { position: absolute; top: 360px; left: 40px; width: 360px; height: 220px; border-radius: 90px / 70px;
    background: radial-gradient(ellipse at center, #ffffff 55%, #cfe9e8 100%); }
  .product-name { position: absolute; top: 400px; left: 0; right: 0; text-align: center; font-family: "Rye", serif;
    font-size: 58px; line-height: 66px; color: var(--teal-deep); letter-spacing: 1px; }

  .descriptor { position: absolute; top: 625px; left: 0; right: 0; text-align: center; }
  .descriptor .kind { display: block; font-size: 22px; font-weight: 400; color: var(--teal); letter-spacing: 0.5px; }
  .descriptor .item { display: block; font-size: 22px; font-weight: 300; color: var(--ink); margin-top: 2px; letter-spacing: 0.5px; }

  .front-web { display: block; margin-top: 74px; font-weight: 700; font-size: 22px; }
  .net-weight { display: block; margin-top: 24px; font-family: "Oswald", sans-serif; font-weight: 300; font-size: 12px; letter-spacing: 3.5px; }
</style>
</head>
<body>
  <div class="box">
    <section class="panel panel-side">
      <div class="side-mark"></div>
      <h2 class="side-title">
        <span class="kind">PREMIUM HERBAL</span>
        <span class="item">Incense Sticks</span>
      </h2>
      <p class="side-copy">Hand-rolled from pure white sage leaves gathered at dawn, each stick burns slowly and evenly for a calm, clean aroma. Light the tip, let it flame briefly, then gently blow it out and set it in the holder. Allow the fragrant smoke to drift through your room during yoga, meditation or quiet prayer. Never leave burning incense unattended and keep it away from children, pets and anything that may catch fire. Store the box in a cool, dry place out of direct sunlight to preserve the scent. Each box holds thirty sticks, twenty-five centimetres long, made with natural binders and no synthetic fillers.</p>
      <div class="band-rule"></div>
      <div class="band">
        <span class="side-web">kelvoro.com.au</span>
      </div>
    </section>

    <section class="panel panel-front">
      <div class="brand">
        <span class="brand-square"></span>
        <span class="brand-name">Kelvoro</span>
      </div>
      <div class="cartouche" role="img" aria-label="Ornamental teal cartouche frame around the product name"></div>
      <h1 class="product-name">WHITE<br>SAGE</h1>
      <p class="descriptor">
        <span class="kind">PREMIUM HERBAL</span>
        <span class="item">Incense Sticks</span>
      </p>
      <div class="band-rule"></div>
      <div class="band">
        <span class="front-web">kelvoro.com.au</span>
        <span class="net-weight">250GRAM/8.8OZ | INCENSE BURNER</span>
      </div>
    </section>
  </div>
</body>
</html>
```